Welding Fabrication and Inspection Business Card Design

Welding Fabrication and Inspection Services,

Business

Industrial Machinery ServicesMohammed Rahim30 Ballarat Street, Mount Gravatt East.4122.QLD

```html
<!DOCTYPE html>
<html lang="en">
<head>
<meta charset="utf-8">
<title>Tarnwell Forge Services – Business Card</title>
<link rel="stylesheet" href="https://fonts.googleapis.com/css2?family=Barlow+Semi+Condensed:wght@700&family=Open+Sans:wght@400;600&display=swap">
<style>
  :root {
    --backdrop: #e9e6e3;
    --card-white: #ffffff;
    --card-black: #000000;
    --ink-dark: #111111;
    --ink-light: #ffffff;
  }
  * { box-sizing: border-box; margin: 0; padding: 0; }
  html, body { width: 1200px; height: 900px; overflow: hidden; }
  body { background: var(--backdrop); position: relative; font-family: "Open Sans", sans-serif; }

  .card {
    position: absolute;
    width: 556px;
    height: 342px;
    overflow: hidden;
    box-shadow: 0 6px 18px rgba(0,0,0,0.18);
  }
  .card--front { left: 238px; top: 62px; background: var(--card-white); }
  .card--back { left: 458px; top: 519px; background: var(--card-black); }

  .brand {
    position: absolute;
    left: 0; right: 0;
    display: flex;
    align-items: center;
    justify-content: center;
    gap: 12px;
    font-family: "Barlow Semi Condensed", sans-serif;
    font-weight: 700;
    font-size: 34px;
    letter-spacing: 0.3px;
  }
  .brand__dot { width: 16px; height: 16px; border-radius: 50%; }
  .card--front .brand { top: 70px; color: var(--ink-dark); }
  .card--front .brand__dot { background: var(--ink-dark); }
  .card--back .brand { top: 140px; color: var(--ink-light); }
  .card--back .brand__dot { background: var(--ink-light); }

  .card__lower {
    position: absolute;
    left: 0; right: 0; top: 178px; bottom: 0;
    background: var(--card-black);
  }
  .card__divider { position: absolute; left: 0; top: 172px; }

  .contact {
    position: absolute;
    left: 0; right: 0; top: 232px;
    text-align: center;
    color: var(--ink-light);
  }
  .contact__name { font-weight: 600; font-size: 19px; line-height: 26px; margin-bottom: 8px; }
  .contact__address { font-weight: 400; font-size: 14.5px; line-height: 19px; }
</style>
</head>
<body>
  <section class="card card--front">
    <div class="brand"><span class="brand__dot"></span>Tarnwell Forge Services</div>
    <div class="card__lower"></div>
    <svg class="card__divider" width="556" height="14" viewBox="0 0 556 14">
      <path d="M0 6 L520 10" stroke="#000" stroke-width="6"/>
      <path d="M0 7.5 L500 10" stroke="#fff" stroke-width="1.6"/>
    </svg>
    <div class="contact">
      <p class="contact__name">Khalid Nasser</p>
      <p class="contact__address">17 Corrowen Street, Kellmore Heights.<br>4198.QLD</p>
    </div>
  </section>

  <section class="card card--back">
    <div class="brand"><span class="brand__dot"></span>Tarnwell Forge Services</div>
  </section>
</body>
</html>
```